Business Card Design Project

2 sided business card utilizing existing logo
- English on one side, Arabic on the other side (both English and Arabic text will be provided)
Same color scheme as logo
Information included will be: name, title, email, phone, address and website (www.veralunix.com)
Updates

Target Market(s)

We are a Systems Integration Company

Industry/Entity Type

Business

Font styles to use
Serif
Sans Serif

Requirements
Should not have
• We prefer using the flat logo rather than one with shadow/3D effect

```html
<!DOCTYPE html>
<html lang="en">
<head>
<meta charset="utf-8">
<title>Veralunix Business Card</title>
<link rel="stylesheet" href="https://fonts.googleapis.com/css2?family=Questrial&display=swap">
<style>
  :root {
    --backdrop: #2a2a2c;
    --card-black: #0d0d0e;
    --card-edge: #1c1c1e;
    --brand-red: #e8232b;
    --text-white: #f2f2f2;
    --divider: #8a8a8a;
  }
  html, body {
    margin: 0;
    padding: 0;
    width: 1200px;
    height: 800px;
    overflow: hidden;
    background: var(--backdrop);
    font-family: "Questrial", "Century Gothic", sans-serif;
  }
  .canvas {
    position: relative;
    width: 1200px;
    height: 800px;
  }
  .card {
    position: absolute;
    left: 150px;
    top: 143px;
    width: 900px;
    height: 514px;
    background: radial-gradient(ellipse at 50% 35%, var(--card-edge) 0%, var(--card-black) 70%);
    box-shadow: 0 20px 50px rgba(0,0,0,0.55);
    overflow: hidden;
  }
  .brand {
    position: absolute;
    left: 0;
    right: 0;
    top: 62px;
    text-align: center;
  }
  .brand-square {
    display: block;
    width: 70px;
    height: 70px;
    margin: 0 auto 22px;
    background: var(--brand-red);
  }
  .brand-name {
    color: var(--brand-red);
    font-size: 46px;
    letter-spacing: 8px;
  }
  .red-band {
    position: absolute;
    left: 0;
    right: 0;
    top: 264px;
    height: 10px;
    background: var(--brand-red);
  }
  .person {
    position: absolute;
    right: 480px;
    top: 318px;
    text-align: right;
  }
  .person-name {
    color: var(--brand-red);
    font-size: 34px;
    margin: 0;
  }
  .person-title {
    color: var(--text-white);
    font-size: 24px;
    margin: 4px 0 0;
  }
  .divider {
    position: absolute;
    left: 448px;
    top: 300px;
    width: 1px;
    height: 160px;
    background: var(--divider);
  }
  .contacts {
    position: absolute;
    left: 470px;
    top: 302px;
    margin: 0;
    padding: 0;
    list-style: none;
    color: var(--text-white);
    font-size: 23px;
    line-height: 33px;
  }
  .contacts li {
    display: flex;
    align-items: flex-start;
  }
  .contacts svg {
    flex: 0 0 22px;
    width: 22px;
    height: 22px;
    margin: 5px 10px 0 0;
    fill: var(--brand-red);
  }
</style>
</head>
<body>
<main class="canvas">
  <section class="card">
    <div class="brand">
      <span class="brand-square"></span>
      <span class="brand-name">VERALUNIX</span>
    </div>

    <div class="red-band"></div>

    <div class="person">
      <p class="person-name">Daran Melk</p>
      <p class="person-title">manager</p>
    </div>

    <div class="divider"></div>

    <ul class="contacts">
      <li>
        <svg viewBox="0 0 24 24" aria-hidden="true"><path d="M6.6 10.8a15 15 0 0 0 6.6 6.6l2.2-2.2a1 1 0 0 1 1-.25 11.4 11.4 0 0 0 3.6.57 1 1 0 0 1 1 1V20a1 1 0 0 1-1 1A17 17 0 0 1 3 4a1 1 0 0 1 1-1h3.5a1 1 0 0 1 1 1c0 1.25.2 2.45.57 3.57a1 1 0 0 1-.25 1z"/></svg>
        <span>(555) 204-7713</span>
      </li>
      <li>
        <svg viewBox="0 0 24 24" aria-hidden="true"><path d="M2 5h20v14H2z M4 7v.5l8 5 8-5V7l-8 5z" fill-rule="evenodd"/></svg>
        <span>info@veralunix.com</span>
      </li>
      <li>
        <svg viewBox="0 0 24 24" aria-hidden="true"><path d="M12 2a10 10 0 1 0 0 20 10 10 0 0 0 0-20zm6.9 6h-2.9a15 15 0 0 0-1.4-3.6A8 8 0 0 1 18.9 8zM12 4c.8 1.2 1.5 2.5 1.9 4h-3.8c.4-1.5 1.1-2.8 1.9-4zM4.3 14a8 8 0 0 1 0-4h3.4a16 16 0 0 0 0 4zm.8 2H8c.3 1.3.8 2.5 1.4 3.6A8 8 0 0 1 5.1 16zM8 8H5.1a8 8 0 0 1 4.3-3.6C8.8 5.5 8.3 6.7 8 8zm4 12c-.8-1.2-1.5-2.5-1.9-4h3.8c-.4 1.5-1.1 2.8-1.9 4zm2.3-6H9.7a14 14 0 0 1 0-4h4.6a14 14 0 0 1 0 4zm.3 5.6c.6-1.1 1.1-2.3 1.4-3.6h2.9a8 8 0 0 1-4.3 3.6zm1.7-5.6a16 16 0 0 0 0-4h3.4a8 8 0 0 1 0 4z"/></svg>
        <span>www.veralunix.com</span>
      </li>
      <li>
        <svg viewBox="0 0 24 24" aria-hidden="true"><path d="M12 3 1 12h3v9h6v-6h4v6h6v-9h3z"/></svg>
        <span>4172 Harlow Lane, Suite D,<br>Maple Springs, CA 90210</span>
      </li>
    </ul>
  </section>
</main>
</body>
</html>
```